Brinevale Yacht Management Full Page Ad Flyer

Yacht Management Package also includes the following periodic Monthly services:

Monthly full vessel systems checklist inspections
Diver For Hull Cleaning And Inspection Of Props, Shafts, and Zincs
Interior/Exterior Detailing and scheduled washdowns
Manage Haulout
Pump-out Services
On-call Captain and Crew Services
Updates

Need more time to provide more content to designers and the printing press template file.

Target Market(s)

Vessel owners, motor yachts, sailboats from 25 feet in length up to 125 feet in length. We do not do cruise ships or yachts larger than 125 feet. Someone who has their boat docked at their house or a local marina. We also offer mobile on-site services.

```html
<!DOCTYPE html>
<html lang="en">
<head>
<meta charset="utf-8">
<title>Brinevale Yacht Management – Flyer</title>
<link href="https://fonts.googleapis.com/css2?family=Crimson+Pro:wght@600&family=Montserrat:wght@400;500&family=Roboto:wght@300;500&family=Source+Sans+3:wght@400&display=swap" rel="stylesheet">
<style>
  :root {
    --stage: #eef0f2;
    --navy: #2b364b;
    --teal: #5fc3c9;
    --white: #ffffff;
    --ink: #0e1a24;
    --body-grey: #6d6f72;
    --list-grey: #7a7c80;
    --footer: #1f252e;
  }
  * { margin: 0; padding: 0; box-sizing: border-box; }
  html, body { width: 998px; height: 1200px; overflow: hidden; background: var(--stage); }
  .flyer {
    position: absolute; left: 76px; top: 0;
    width: 846px; height: 1200px;
    background: var(--white); overflow: hidden;
  }
  .header { position: absolute; left: 0; top: 0; width: 846px; height: 475px; }
  .header svg { position: absolute; left: 0; top: 0; }
  .brand {
    position: absolute; top: 62px; left: 0; width: 100%;
    text-align: center; color: var(--teal);
    font-family: "Montserrat", sans-serif; font-weight: 500;
  }
  .brand-name { display: block; font-size: 36px; letter-spacing: 3px; line-height: 40px; }
  .brand-tag { display: block; font-size: 10.5px; letter-spacing: 2.6px; margin-top: 2px; }
  .headline {
    position: absolute; top: 150px; left: 0; width: 100%;
    text-align: center; color: var(--white);
    font-family: "Crimson Pro", serif; font-weight: 600;
    font-size: 62px; line-height: 77px;
  }
  .package-title {
    position: absolute; top: 494px; left: 0; width: 100%;
    text-align: center; color: var(--ink);
    font-family: "Source Sans 3", sans-serif; font-weight: 400;
    font-size: 34px; line-height: 44px;
  }
  .intro {
    position: absolute; top: 593px; left: 40px; width: 766px;
    text-align: center; color: var(--body-grey);
    font-family: "Roboto", sans-serif; font-weight: 500;
    font-size: 21.5px; line-height: 27.5px;
  }
  .services-label {
    position: absolute; top: 717px; left: 321px; width: 204px; height: 47px;
    border: 2.5px solid var(--teal); border-radius: 4px;
    text-align: center; line-height: 42px; color: var(--ink);
    font-family: "Source Sans 3", sans-serif; font-size: 30px;
  }
  .service-list {
    position: absolute; top: 772px; left: 0; width: 100%;
    list-style: none; text-align: center; color: var(--list-grey);
    font-family: "Roboto", sans-serif; font-weight: 300;
    font-size: 19.5px; line-height: 28.4px;
  }
  .yacht-photo {
    position: absolute; left: 0; top: 1022px; width: 846px; height: 113px;
    background: linear-gradient(180deg, #3e4346 0%, #4c4a47 55%, #2e3236 100%);
  }
  .yacht-photo::before {
    content: ""; position: absolute; left: 60px; top: -104px; width: 720px; height: 200px;
    border-radius: 50% 50% 8% 8% / 40% 40% 10% 10%;
    background: linear-gradient(180deg, rgba(200,190,180,0.0) 0%, rgba(176,150,130,0.55) 55%, rgba(120,100,90,0.6) 100%);
  }
  .contact-bar {
    position: absolute; left: 0; top: 1135px; width: 846px; height: 65px;
    background: var(--footer); color: var(--white);
    font-family: "Montserrat", sans-serif; font-weight: 400; font-size: 15.5px;
  }
  .contact-bar span, .contact-bar svg { position: absolute; }
  .contact-label { left: 99px; top: 23px; letter-spacing: 0.8px; }
  .contact-phone { left: 336px; top: 23px; letter-spacing: 0.5px; }
  .contact-web { left: 528px; top: 23px; }
  .icon-phone { left: 309px; top: 24px; }
  .icon-web { left: 508px; top: 24px; }
</style>
</head>
<body>
  <main class="flyer">
    <header class="header">
      <svg width="846" height="475" viewBox="0 0 846 475" aria-hidden="true">
        <path d="M0 0 H846 V408 Q423 440 0 418 Z" fill="#2b364b"/>
        <path d="M0 418 Q423 440 846 408 V424 Q423 457 0 434 Z" fill="#ffffff"/>
        <path d="M0 434 Q423 457 846 424 V440 Q423 476 0 452 Z" fill="#2b364b"/>
      </svg>
      <div class="brand">
        <span class="brand-name">BRINEVALE</span>
        <span class="brand-tag">YACHT MANAGEMENT</span>
      </div>
      <h1 class="headline">Find Tranquility and<br>experience the<br>beauty of the Sea</h1>
    </header>

    <h2 class="package-title">Yacht Management Package Also Includes The<br>Following Periodic Monthly</h2>
    <p class="intro">Discover the convenience and excellent service of BRINEVALE yacht management, always check the fitness of your boat, avoid damage that causes discomfort and comfort on the cruise.</p>

    <div class="services-label">Services</div>
    <ul class="service-list">
      <li>Monthly full vessel systems checklist inspections</li>
      <li>Diver For Hull Cleaning And Inspection Of Props, Shafts, and Zincs,</li>
      <li>Interior/Exterior Detailing and scheduled washdowns,</li>
      <li>Manage Haulout, Pump-out Services, On-call Captain and Crew Services</li>
    </ul>

    <div class="yacht-photo" role="img" aria-label="Photo of a luxury motor yacht at anchor on calm water at dusk"></div>

    <footer class="contact-bar">
      <span class="contact-label">CONTACT US</span>
      <svg class="icon-phone" width="18" height="18" viewBox="0 0 24 24" aria-hidden="true">
        <path d="M6.6 3.5l2.6 3.2-1.6 2.2c1.2 2.6 3.3 4.7 5.9 5.9l2.2-1.6 3.2 2.6-1.4 3C10.8 19 5 13.2 4.7 4.9z" fill="none" stroke="#fff" stroke-width="1.4" stroke-linejoin="round"/>
        <path d="M14 4a6 6 0 0 1 6 6M14 7.2a2.8 2.8 0 0 1 2.8 2.8" fill="none" stroke="#fff" stroke-width="1.3"/>
      </svg>
      <span class="contact-phone">+614-5550-0198</span>
      <svg class="icon-web" width="18" height="18" viewBox="0 0 24 24" aria-hidden="true">
        <circle cx="12" cy="12" r="10" fill="none" stroke="#fff" stroke-width="1.4"/>
        <ellipse cx="12" cy="12" rx="4.5" ry="10" fill="none" stroke="#fff" stroke-width="1.3"/>
        <path d="M2 12h20M4 7h16M4 17h16" stroke="#fff" stroke-width="1.2"/>
      </svg>
      <span class="contact-web">www.brinevaleyachts.com.au</span>
    </footer>
  </main>
</body>
</html>
```